Thank You Card

I'm looking for a thank you card design using our logo and other graphics. We are an essential business and our employees (Electricians) have done an incredible job staying healthy and safe during the COVID-19 pandemic, I want to send each a thank you card.

```html
<!DOCTYPE html>
<html lang="en">
<head>
<meta charset="utf-8">
<title>Thank You Card</title>
<link rel="stylesheet" href="https://fonts.googleapis.com/css2?family=Open+Sans:wght@700&family=Poppins:wght@300;600&display=swap">
<style>
  :root {
    --page-bg: #d4d4d4;
    --card-red: #b9000b;
    --card-white: #ebeaec;
    --ink-white: #ebeaec;
    --ink-red: #c10812;
  }
  * { margin: 0; padding: 0; box-sizing: border-box; }
  html, body {
    width: 1200px;
    height: 1068px;
    overflow: hidden;
    background: var(--page-bg);
  }
  .card {
    position: absolute;
    left: 50px;
    top: 154px;
    width: 1100px;
    height: 760px;
    background: var(--card-white);
    overflow: hidden;
  }
  .card__red-panel {
    position: absolute;
    left: 0;
    top: 0;
    width: 634px;
    height: 100%;
    background: var(--card-red);
  }
  .headline {
    position: absolute;
    top: 191px;
    font-family: "Open Sans", sans-serif;
    font-weight: 700;
    font-size: 176px;
    line-height: 1;
    letter-spacing: -2px;
    white-space: nowrap;
  }
  .headline--thank {
    right: 466px;
    color: var(--ink-white);
  }
  .headline--you {
    left: 634px;
    color: var(--ink-red);
  }
  .bulb-base {
    position: absolute;
    left: 789px;
    width: 45px;
    height: 10px;
    background: var(--ink-red);
  }
  .bulb-base--top { top: 358px; }
  .bulb-base--bottom { top: 375px; }
  .virus-graphic {
    position: absolute;
    left: 43px;
    top: 557px;
    width: 76px;
    height: 150px;
    background: rgba(255, 255, 255, 0.14);
    border-radius: 75px 0 0 75px;
  }
  .divider {
    position: absolute;
    left: 117px;
    top: 557px;
    width: 3px;
    height: 150px;
    background: rgba(255, 255, 255, 0.25);
  }
  .message {
    position: absolute;
    left: 153px;
    top: 578px;
    font-family: "Poppins", sans-serif;
    font-weight: 300;
    font-size: 30px;
    line-height: 36px;
    color: var(--ink-white);
  }
  .company-name {
    position: absolute;
    left: 634px;
    width: 466px;
    top: 622px;
    text-align: center;
    font-family: "Poppins", sans-serif;
    font-weight: 600;
    font-size: 34px;
    line-height: 1;
    color: var(--ink-red);
  }
</style>
</head>
<body>
  <div class="card">
    <div class="card__red-panel"></div>
    <div class="headline headline--thank">thank</div>
    <div class="headline headline--you">you</div>
    <div class="bulb-base bulb-base--top"></div>
    <div class="bulb-base bulb-base--bottom"></div>
    <div class="virus-graphic" role="img" aria-label="Faint half coronavirus illustration"></div>
    <div class="divider"></div>
    <p class="message">for staying healthy<br>&amp; safe during<br>COVID-19 pandemic</p>
    <div class="company-name">Brightline Electric</div>
  </div>
</body>
</html>
```